Brightwell Wiring Needs A Logo Design

We need a logo for my new company based out of Sacramento, Ca called Brightwell Wiring. The name says it all, my electrical contracting business provides "Brightwell Craftsman Work" I'm open to any colors that pop and customers to say Wow. I would love to print my cards on metal.

Contact Information for Business Card

The card needs to have as follows
Name of company: Brightwell Wiring
My Name: Marco Delvane
Phone # 916-555-0147
CL# 4873920
Email: brightwellwiring@mailtorva.com
and a slogan that represent "BRIGHTWELL"

Requirements
Must have
• The card needs to have as follows
• Name of company: Brightwell Wiring
• My Name : Marco Delvane
• Phone # 916-555-0147
• CL# 4873920
• Email: brightwellwiring@mailtorva.com
• and a slogan that represent "BRIGHTWELL"
Nice to have
• popping colors
• electrical Arcing

```html
<!DOCTYPE html>
<html lang="en">
<head>
<meta charset="utf-8">
<title>Brightwell Wiring – Business Card</title>
<link href="https://fonts.googleapis.com/css2?family=Roboto+Slab:wght@700&family=Open+Sans:wght@400;700&display=swap" rel="stylesheet">
<style>
  :root {
    --page-bg: #2a2827;
    --card-top: #050608;
    --card-bottom: #17191c;
    --brand-blue: #1f86d0;
    --band-text: #0a1a33;
    --muted: #a9adb2;
    --contact: #c9ccd0;
    --arc-deep: #0a0d2e;
    --arc-mid: #27328a;
    --arc-glow: #9fb4ff;
  }
  * { box-sizing: border-box; margin: 0; padding: 0; }
  html, body { width: 1200px; height: 1200px; overflow: hidden; }
  body {
    background: var(--page-bg);
    font-family: "Open Sans", Arial, sans-serif;
    position: relative;
  }
  .card {
    position: absolute;
    left: 100px; top: 314px;
    width: 1000px; height: 572px;
    background: var(--card-bottom);
    overflow: hidden;
    box-shadow: 0 10px 30px rgba(0,0,0,.5);
  }
  .card__header {
    position: absolute; left: 0; top: 0;
    width: 100%; height: 222px;
    background: var(--card-top);
  }
  .card__arc-visual {
    position: absolute; right: 0; top: 0;
    width: 470px; height: 222px;
    background: radial-gradient(ellipse at 80% 45%, var(--arc-glow) 0%, var(--arc-mid) 25%, var(--arc-deep) 60%, var(--card-top) 100%);
  }
  .brand-name {
    position: absolute; left: 80px; top: 78px;
    font-family: "Roboto Slab", Georgia, serif;
    font-weight: 700;
    font-size: 64px;
    color: var(--brand-blue);
    letter-spacing: 1px;
  }
  .slogan-band {
    position: absolute; left: 0; top: 222px;
    width: 100%; height: 40px;
    background: var(--brand-blue);
    display: flex; align-items: center; justify-content: flex-end;
    padding-right: 200px;
  }
  .slogan-band__text {
    font-weight: 700; font-size: 22px;
    color: var(--band-text);
    text-transform: uppercase;
  }
  .person {
    position: absolute; left: 80px; top: 300px;
  }
  .person__name {
    font-family: "Roboto Slab", Georgia, serif;
    font-weight: 700; font-size: 36px;
    color: var(--brand-blue);
    text-transform: uppercase;
    letter-spacing: 1px;
  }
  .person__title {
    margin-top: 4px;
    font-size: 22px;
    color: var(--muted);
    text-transform: uppercase;
  }
  .divider {
    position: absolute; left: 420px; top: 292px;
    width: 2px; height: 180px;
    background: var(--brand-blue);
  }
  .contact {
    position: absolute; left: 460px; top: 370px;
    list-style: none;
  }
  .contact__item {
    display: flex; align-items: center; gap: 14px;
    font-size: 26px; line-height: 40px;
    color: var(--contact);
  }
  .contact__icon { width: 22px; height: 22px; flex: none; }
  .contact__label {
    font-weight: 700; color: var(--brand-blue);
  }
</style>
</head>
<body>
  <section class="card" aria-label="Brightwell Wiring business card">
    <div class="card__header">
      <div class="card__arc-visual" role="img" aria-label="Photograph of electric lightning arcs"></div>
      <div class="brand-name">Brightwell Wiring</div>
    </div>
    <div class="slogan-band"><span class="slogan-band__text">Brightwell Craftsman Work</span></div>

    <div class="person">
      <div class="person__name">Marco Delvane</div>
      <div class="person__title">Owner</div>
    </div>

    <div class="divider"></div>

    <ul class="contact">
      <li class="contact__item">
        <svg class="contact__icon" viewBox="0 0 24 24" aria-hidden="true"><rect width="24" height="24" rx="4" fill="#1f86d0"/><path d="M8 5l2.5 3-1.5 2c1 2 2.5 3.5 4.5 4.5l2-1.5 3 2.5-1.5 2.5C12 18 6 12 5.5 6.5z" fill="#17191c"/></svg>
        <span>916-555-0147</span>
      </li>
      <li class="contact__item">
        <svg class="contact__icon" viewBox="0 0 24 24" aria-hidden="true"><rect width="24" height="24" rx="4" fill="#1f86d0"/><rect x="5" y="7" width="14" height="10" fill="none" stroke="#17191c" stroke-width="2"/><path d="M5 7l7 6 7-6" fill="none" stroke="#17191c" stroke-width="2"/></svg>
        <span>brightwellwiring@mailtorva.com</span>
      </li>
      <li class="contact__item">
        <span class="contact__label">CL#</span>
        <span>4873920</span>
      </li>
    </ul>
  </section>
</body>
</html>
```